Visitenkarten für ein Metallverarbeitsungsbetrieb
Zielgruppe
Metallverarbeitsungsbetrieb
spezialisiert auf Lasern
Aufgabenstellung
Passend zu unseren Logo und in den Farben, schlicht dennoch besonders

```html
<!DOCTYPE html>
<html lang="de">
<head>
<meta charset="utf-8">
<title>Kerbon Laser GmbH – Visitenkarten</title>
<link rel="stylesheet" href="https://fonts.googleapis.com/css2?family=Montserrat:wght@400;500;700&display=swap">
<style>
  :root {
    --page-bg: #e9edf0;
    --card-bg: #ffffff;
    --brand-blue: #1a7db5;
    --text-grey: #5f5f62;
    --text-dark: #4a4a4d;
  }
  * { box-sizing: border-box; margin: 0; padding: 0; }
  html, body {
    width: 1200px;
    height: 1200px;
    overflow: hidden;
    background: var(--page-bg);
    font-family: "Montserrat", sans-serif;
  }
  .sheet {
    position: relative;
    width: 1200px;
    height: 1200px;
  }
  .card {
    position: absolute;
    left: 180px;
    width: 840px;
    height: 540px;
    background: var(--card-bg);
  }
  .card--front { top: 40px; }
  .card--back { top: 620px; }

  .wordmark {
    display: flex;
    align-items: center;
    gap: 22px;
  }
  .wordmark__dot {
    flex: none;
    border: 8px solid var(--brand-blue);
    border-radius: 50%;
  }
  .wordmark__name {
    font-weight: 700;
    color: var(--text-grey);
    white-space: nowrap;
  }
  .card--front .wordmark {
    position: absolute;
    left: 50%;
    top: 50%;
    transform: translate(-50%, -50%);
  }
  .card--front .wordmark__dot { width: 120px; height: 120px; }
  .card--front .wordmark__name { font-size: 44px; }

  .card--back .wordmark {
    position: absolute;
    right: 64px;
    bottom: 56px;
    gap: 14px;
  }
  .card--back .wordmark__dot { width: 72px; height: 72px; border-width: 6px; }
  .card--back .wordmark__name { font-size: 24px; }

  .contact {
    position: absolute;
    left: 62px;
    top: 74px;
    color: var(--text-grey);
  }
  .contact__name {
    font-size: 27px;
    font-weight: 700;
    letter-spacing: 2px;
    color: var(--text-dark);
  }
  .contact__role {
    margin-top: 4px;
    font-size: 21px;
    font-weight: 500;
    color: var(--brand-blue);
  }
  .contact__address {
    margin-top: 38px;
    font-size: 20px;
    line-height: 45px;
  }
  .contact__lines {
    list-style: none;
    margin-top: 18px;
    font-size: 20px;
  }
  .contact__lines li {
    display: flex;
    align-items: center;
    gap: 18px;
    height: 45px;
  }
  .contact__icon {
    width: 24px;
    height: 24px;
    fill: none;
    stroke: var(--text-grey);
    stroke-width: 1.6;
    stroke-linecap: round;
    stroke-linejoin: round;
  }
</style>
</head>
<body>
<main class="sheet">

  <section class="card card--front" aria-label="Vorderseite">
    <div class="wordmark">
      <span class="wordmark__dot"></span>
      <span class="wordmark__name">Kerbon Laser GmbH</span>
    </div>
  </section>

  <section class="card card--back" aria-label="Rückseite">
    <div class="contact">
      <p class="contact__name">JONAS</p>
      <p class="contact__role">Manager</p>
      <p class="contact__address">#1234 Your Location Here<br>Your RD. Your Street Postal 56162</p>
      <ul class="contact__lines">
        <li>
          <svg class="contact__icon" viewBox="0 0 24 24" aria-hidden="true">
            <path d="M5 3h4l2 5-2.5 1.5a11 11 0 0 0 6 6L16 13l5 2v4a2 2 0 0 1-2 2A16 16 0 0 1 3 5a2 2 0 0 1 2-2z"/>
            <path d="M15 3a6 6 0 0 1 6 6M15 7a2 2 0 0 1 2 2"/>
          </svg>
          <span>+00 11 22 33 44 55</span>
        </li>
        <li>
          <svg class="contact__icon" viewBox="0 0 24 24" aria-hidden="true">
            <rect x="3" y="5" width="18" height="14" rx="1.5"/>
            <path d="M3 6l9 7 9-7"/>
          </svg>
          <span>info@yourmail.com</span>
        </li>
        <li>
          <svg class="contact__icon" viewBox="0 0 24 24" aria-hidden="true">
            <circle cx="12" cy="12" r="9"/>
            <path d="M3 12h18M12 3c3 3 3 15 0 18M12 3c-3 3-3 15 0 18"/>
          </svg>
          <span>www.webname.com</span>
        </li>
      </ul>
    </div>
    <div class="wordmark">
      <span class="wordmark__dot"></span>
      <span class="wordmark__name">Kerbon Laser GmbH</span>
    </div>
  </section>

</main>
</body>
</html>
```